Design a web site for my business - Brellan Coatworks Mackaby.

We are a family business that handles design, fabrication and installation of powder coated aluminum, stainless steel and glass products. Including handrails, privacy slat screens, electric gates and pool fencing. We are based in the Whitsundays in North Queensland and service an area from Airlie Beach to Townsville.

Target Market(s)

Domestic and commercial

Industry/Entity Type

fabrication - manufacturing

Coding

Coded - Design and coding required

Number of Pages Required

5+ page

Colors
0054AA
0677BA
7BADD7
CADEEF
E8F1F8

Requirements
Must have
• photo galleries, contact page, one page for privacy screens, balustrades, glass fencing, stainless steel handrail, powder coated aluminium handrails and pool fencing

```html
<!DOCTYPE html>
<html lang="en">
<head>
<meta charset="utf-8">
<title>Your Business — Aluminium, Stainless Steel & Glass</title>
<link href="https://fonts.googleapis.com/css2?family=Bebas+Neue&family=Poppins:wght@300;400;500;600&display=swap" rel="stylesheet">
<style>
:root{
  --blue-deep:#0054AA;
  --blue:#0677BA;
  --blue-light:#7BADD7;
  --blue-pale:#CADEEF;
  --blue-mist:#E8F1F8;
  --navy:#071a33;
  --navy-soft:#0b2444;
  --white:#ffffff;
  --text:#1f2a38;
  --muted:#5a6675;
}
*{box-sizing:border-box;margin:0;padding:0}
html,body{width:1200px;height:5319px;overflow:hidden}
body{font-family:'Poppins',sans-serif;color:var(--text);background:var(--blue-mist);position:relative}
.display{font-family:'Bebas Neue',sans-serif;font-weight:400;letter-spacing:.5px}
section,header,footer{position:relative;width:1200px;overflow:hidden}
.abs{position:absolute}
.btn{position:absolute;display:flex;align-items:center;justify-content:center;gap:6px;background:var(--blue);color:var(--white);font-size:12px;font-weight:600;letter-spacing:.5px;text-transform:uppercase}
.btn-outline{background:transparent;border:1.5px solid var(--white)}
.divider{position:absolute;height:3px;width:92px;background:var(--blue)}
.eyebrow{position:absolute;font-size:13px;letter-spacing:2px;text-transform:uppercase;color:var(--blue)}

/* HERO */
.hero{height:744px;background:linear-gradient(180deg,#4a5560 0%,#8b7360 30%,#3a3633 62%,#1c1b1a 100%)}
.hero-photo{position:absolute;inset:0;background:linear-gradient(100deg,rgba(7,26,51,.75) 0%,rgba(7,26,51,.2) 45%,rgba(230,160,100,.25) 70%,rgba(30,30,30,.4) 100%)}
.nav{position:absolute;top:20px;left:128px;right:128px;height:44px;display:flex;align-items:center}
.logo{display:flex;align-items:center;gap:10px;color:var(--white);font-size:19px;font-weight:500;letter-spacing:.5px}
.logo-mark{width:26px;height:26px;border:2px solid var(--blue-light)}
.nav-links{display:flex;gap:40px;margin-left:52px;font-size:11px;color:var(--white);text-transform:uppercase;letter-spacing:.5px}
.nav .btn{position:static;margin-left:auto;width:146px;height:40px}
.hero h1{position:absolute;left:116px;top:188px;font-size:62px;line-height:57px;color:var(--white)}
.hero .eyebrow{left:118px;top:162px;letter-spacing:1px;color:var(--blue-light)}
.hero p.lead{position:absolute;left:118px;top:370px;width:440px;color:#e6eef6;font-size:12.5px;line-height:19px}
.hero-feats{position:absolute;left:118px;top:518px;display:flex;gap:28px;color:var(--white);font-size:10px;font-weight:600;text-transform:uppercase;line-height:13px}
.hero-feats div{display:flex;align-items:center;gap:9px}

/* SERVICES */
.services{height:888px}
.services h2{position:absolute;left:0;right:0;top:22px;text-align:center;font-size:50px;line-height:56px;color:var(--navy)}
.card{position:absolute;background:var(--blue-pale)}
.card .photo{height:192px}
.card .body{position:relative;padding:16px 16px 0 80px;height:123px}
.card .icon{position:absolute;left:22px;top:30px;width:40px;height:40px}
.card h3{font-family:'Bebas Neue',sans-serif;font-weight:400;font-size:20px;color:var(--navy);margin-bottom:6px}
.card p{font-size:9.5px;line-height:14px;color:var(--muted);width:160px}
.card .explore{display:block;margin-top:10px;font-size:9px;letter-spacing:1px;color:var(--blue-deep);font-weight:600}

/* ABOUT */
.about{height:630px;background:var(--navy)}
.about .eyebrow{color:var(--blue-light)}
.about h2{position:absolute;left:660px;top:128px;font-size:52px;line-height:50px;color:var(--white)}
.about p{position:absolute;left:660px;width:450px;font-size:14px;line-height:25px;color:#e2eaf3}
.stat{position:absolute;top:423px;color:var(--white)}
.stat b{display:block;font-weight:400;font-size:36px;line-height:40px}
.stat span{font-size:11px;font-weight:600;text-transform:uppercase}

/* PROCESS */
.process{height:800px;background:var(--blue-mist)}
.process h2{position:absolute;left:128px;top:80px;font-size:56px;color:var(--navy)}
.process p.intro{position:absolute;left:128px;top:176px;width:420px;font-size:14px;line-height:25px;color:var(--text)}
.step{position:absolute;left:128px;display:flex;gap:14px;align-items:flex-start}
.step .num{color:var(--blue);font-size:17px;width:30px;margin-top:4px}
.step h4{font-size:17px;font-weight:500;color:var(--navy)}
.step span{font-size:12.5px;color:var(--muted)}

/* TESTIMONIALS */
.testimonials{height:599px;background:var(--navy-soft)}
.testimonials h2{position:absolute;left:0;right:0;top:58px;text-align:center;font-size:56px;color:var(--white)}
.testimonials .divider{background:var(--blue-light)}
.quote{position:absolute;top:171px;width:464px;height:262px;border:1px solid var(--blue-light);padding:30px 56px 0 56px;color:var(--white)}
.quote p{font-size:18px;line-height:29px;margin-top:14px}
.quote .stars{color:var(--blue-light);font-size:17px;letter-spacing:2px;margin-top:8px;line-height:18px}
.quote .name{font-size:13px;font-weight:600}

/* AREAS */
.areas{height:657px;background:var(--blue-mist)}
.areas h2{position:absolute;left:0;right:0;top:38px;text-align:center;font-size:56px;color:var(--navy)}
.areas-card{position:absolute;left:107px;top:159px;width:505px;height:420px;background:var(--white)}
.areas-card h3{position:absolute;left:83px;top:48px;font-family:'Bebas Neue',sans-serif;font-weight:400;font-size:38px;color:var(--navy)}
.area-list{position:absolute;left:83px;top:108px;width:330px;list-style:none}
.area-list li{height:42px;border-bottom:1px solid #d5e2ee;display:flex;align-items:center;gap:14px;font-size:19px;color:var(--navy);padding-left:10px}
.area-list li:last-child{border:none}

/* CONTACT */
.contact{height:547px;background:linear-gradient(115deg,#0677BA 0%,#0054AA 40%,#1f84c4 70%,#0054AA 100%)}
.contact h2{position:absolute;left:135px;top:90px;font-size:54px;color:var(--white)}
.c-item{position:absolute;left:138px;display:flex;gap:12px;color:var(--white)}
.c-item .ic{width:40px;height:40px;border-radius:50%;background:var(--white);display:flex;align-items:center;justify-content:center;flex:none}
.c-item b{display:block;font-weight:500;font-size:17px}
.c-item span{font-size:17px;font-weight:300}
.form h3{position:absolute;left:595px;top:80px;font-family:'Bebas Neue',sans-serif;font-weight:400;font-size:40px;color:var(--white)}
.label{position:absolute;font-size:13px;color:var(--white)}
.field{position:absolute;height:46px;background:var(--white);font-size:12px;color:#555;padding:14px 16px}

/* FOOTER */
.footer{height:454px;background:var(--navy);color:var(--white)}
.footer h5{font-family:'Bebas Neue',sans-serif;font-weight:400;font-size:19px;padding-left:10px;border-left:1px solid var(--white);margin-bottom:12px}
.f-col{position:absolute;top:140px}
.f-col ul{list-style:none;padding-left:10px;font-size:11px;line-height:19px;color:#d4e0ec}
.f-bottom{position:absolute;top:410px;left:117px;right:117px;display:flex;justify-content:space-between;font-size:10px;color:#9fb3c8;border-top:1px solid #1d3656;padding-top:10px}
</style>
</head>
<body>

<header class="hero">
  <div class="hero-photo" role="img" aria-label="Modern home entrance at sunset with black slat gate overlooking the ocean"></div>
  <nav class="nav">
    <div class="logo"><span class="logo-mark"></span>YOUR BUSINESS</div>
    <div class="nav-links"><span>About</span><span>Services</span><span>Gallery</span><span>Areas We Service</span><span>Contact</span></div>
    <a class="btn">Get a Quote ↗</a>
  </nav>
  <div class="eyebrow">Your Business Name</div>
  <h1 class="display">Quality Aluminium,<br>Stainless Steel &amp;<br>Glass Solutions</h1>
  <p class="lead">From concept to completion, we design, fabricate and install premium powder coated aluminium, stainless steel and glass products</p>
  <a class="btn" style="left:118px;top:430px;width:186px;height:48px">Get a Free Quote ↗</a>
  <a class="btn btn-outline" style="left:316px;top:430px;width:208px;height:48px">
    <svg width="14" height="14" viewBox="0 0 24 24" fill="#fff"><path d="M6.6 10.8a15 15 0 006.6 6.6l2.2-2.2a1 1 0 011-.25 11 11 0 003.5.56 1 1 0 011 1V20a1 1 0 01-1 1A17 17 0 013 4a1 1 0 011-1h3.5a1 1 0 011 1 11 11 0 00.56 3.5 1 1 0 01-.25 1z"/></svg>Call 0491 570 006</a>
  <div class="hero-feats">
    <div><svg width="22" height="22"><rect x="2" y="6" width="18" height="14" fill="var(--blue-light)"/></svg>Family Owned<br>&amp; Operated</div>
    <div><svg width="22" height="22"><circle cx="11" cy="9" r="7" fill="var(--blue-light)"/><rect x="7" y="14" width="8" height="7" fill="var(--blue-light)"/></svg>Quality<br>Workmanship</div>
    <div><svg width="22" height="22"><path d="M2 12 C6 4 16 3 20 9 L18 19 L6 18 Z" fill="var(--blue-light)"/></svg>Built to Austrlian<br>Standard</div>
  </div>
  <svg class="abs" style="left:0;top:620px" width="1200" height="124" viewBox="0 0 1200 124">
    <defs><linearGradient id="band" x1="0" x2="1"><stop offset="0" stop-color="#7BADD7"/><stop offset="1" stop-color="#0054AA"/></linearGradient></defs>
    <polygon points="0,124 620,6 1200,80 1200,124" fill="url(#band)"/>
    <polygon points="0,124 640,22 1200,88 1200,124" fill="var(--blue-mist)"/>
  </svg>
</header>

<section class="services">
  <div class="eyebrow" style="left:0;right:0;text-align:center;top:0">Our Services</div>
  <h2 class="display">Complete Design, Fabrication<br>&amp; Installation Services</h2>
  <div class="divider" style="left:554px;top:140px"></div>

  <div class="card" style="left:58px;top:181px;width:265px">
    <div class="photo" role="img" aria-label="Glass and stainless steel staircase handrail" style="background:linear-gradient(135deg,#e8e6e2,#9aa0a3)"></div>
    <div class="body"><svg class="icon" viewBox="0 0 40 40" fill="none" stroke="var(--blue)" stroke-width="1.5"><path d="M4 34h10v-8h8v-8h10"/><path d="M6 28L30 8"/></svg>
      <h3>Handrails</h3><p>Safe, stylish and built to last. Custom handrails in aluminium, stainless steel and glass.</p><span class="explore">EXPLORE ⟶</span></div>
  </div>
  <div class="card" style="left:335px;top:181px;width:265px">
    <div class="photo" role="img" aria-label="Black electric slat gate at a tropical driveway" style="background:linear-gradient(135deg,#8fae8a,#2a2d2a)"></div>
    <div class="body"><svg class="icon" viewBox="0 0 40 40" fill="none" stroke="var(--blue)" stroke-width="1.5"><rect x="4" y="10" width="32" height="22"/><path d="M12 10v22M20 10v22M28 10v22"/></svg>
      <h3>Electric Gates</h3><p>Automatic gates designed for security, convenience and peace of mind.</p><span class="explore">EXPLORE ⟶</span></div>
  </div>
  <div class="card" style="left:610px;top:181px;width:260px">
    <div class="photo" role="img" aria-label="Black aluminium privacy slat screen with palms" style="background:linear-gradient(135deg,#3a3f38,#0e100e)"></div>
    <div class="body"><svg class="icon" viewBox="0 0 40 40" fill="none" stroke="var(--blue)" stroke-width="1.5"><rect x="6" y="6" width="28" height="28"/><path d="M6 13h28M6 20h28M6 27h28"/></svg>
      <h3>Privacy Screens</h3><p>Sleek aluminium slat screens for privacy, shade and architectural style.</p><span class="explore">EXPLORE ⟶</span></div>
  </div>
  <div class="card" style="left:880px;top:181px;width:250px">
    <div class="photo" role="img" aria-label="Glass pool fence beside an ocean view pool" style="background:linear-gradient(180deg,#7fb3d8,#2d8db4)"></div>
    <div class="body"><svg class="icon" viewBox="0 0 40 40" fill="none" stroke="var(--blue)" stroke-width="1.5"><rect x="6" y="8" width="10" height="26"/><rect x="24" y="8" width="10" height="26"/><path d="M16 14h8M16 28h8"/></svg>
      <h3>Pool Fencing</h3><p>Beautiful, compliant pool fencing that enhances your space and protects your family.</p><span class="explore">EXPLORE ⟶</span></div>
  </div>

  <div class="card" style="left:170px;top:521px;width:270px;height:275px">
    <div class="photo" role="img" aria-label="Frameless glass balustrade on a balcony overlooking islands" style="height:152px;background:linear-gradient(180deg,#8fbfdc,#3a7fa0)"></div>
    <div class="body"><svg class="icon" viewBox="0 0 40 40" fill="none" stroke="var(--blue)" stroke-width="1.5"><rect x="6" y="6" width="28" height="28"/><path d="M10 6v28M30 6v28"/></svg>
      <h3>Glass Balustrades</h3><p>Frameless and semi-frameless glass balustrades for uninterrupted views and luxury finishes.</p><span class="explore">EXPLORE ⟶</span></div>
  </div>
  <div class="card" style="left:450px;top:521px;width:285px;height:275px">
    <div class="photo" role="img" aria-label="Stainless steel railing at a seaside sunset" style="height:152px;background:linear-gradient(180deg,#c9b39a,#6a7c8a)"></div>
    <div class="body"><svg class="icon" viewBox="0 0 40 40" fill="none" stroke="var(--blue)" stroke-width="1.5"><circle cx="14" cy="26" r="6"/><path d="M18 22L32 8M26 8h6v6"/></svg>
      <h3>Stainless Steel</h3><p>Corrosion resistant and built for strength in coastal environments.</p><span class="explore">EXPLORE ⟶</span></div>
  </div>
  <div class="card" style="left:745px;top:521px;width:273px;height:275px">
    <div class="photo" role="img" aria-label="Worker welding aluminium in a workshop" style="height:152px;background:linear-gradient(135deg,#2b4358,#0f1820)"></div>
    <div class="body"><svg class="icon" viewBox="0 0 40 40" fill="none" stroke="var(--blue)" stroke-width="1.5"><rect x="8" y="8" width="24" height="24" rx="8"/><path d="M14 20h12"/></svg>
      <h3>Aluminium Fabrication</h3><p>Custom fabricated aluminium solutions and architectural features made in-house.</p><span class="explore">EXPLORE ⟶</span></div>
  </div>
</section>

<section class="about">
  <div class="abs" role="img" aria-label="Installer fitting a black slat gate at a modern home" style="left:0;top:0;width:600px;height:630px;clip-path:polygon(0 0,420px 0,600px 200px,360px 630px,0 630px);background:linear-gradient(135deg,#c9cfd2,#6f7a6a 60%,#3d4a3a)"></div>
  <div class="eyebrow" style="left:660px;top:102px;font-size:12px">About Company</div>
  <h2 class="display">Family Owned.<br>Quality Focused</h2>
  <p style="top:256px">As a locally owned family business, we take pride in delivering high-quality metal and glass solutions that are built to perform and designed to complement your property.</p>
  <p style="top:340px">From the initial design consultation through fabrication and professional installation, every project is completed</p>
  <div class="stat display" style="left:667px"><b>20+</b><span style="font-family:Poppins,sans-serif">Years of Experience</span></div>
  <div class="abs" style="left:848px;top:420px;width:1px;height:62px;background:#4a6484"></div>
  <div class="stat display" style="left:886px"><b>1000+</b><span style="font-family:Poppins,sans-serif">Thousands of Installations</span></div>
</section>

<section class="process">
  <h2 class="display">Our Process</h2>
  <p class="intro">From the initial design consultation through fabrication and professional installation, every project is completed with precision, attention</p>
  <div class="step" style="top:290px"><svg width="40" height="40" fill="none" stroke="var(--blue)" stroke-width="1.5"><path d="M6 6l28 28M34 6L6 34"/></svg><span class="num">01</span><div><h4>Design</h4><span>Lorem ipsum dolor sit amet consectetur adipiscing</span></div></div>
  <div class="step" style="top:364px"><svg width="40" height="40" fill="none" stroke="var(--blue)" stroke-width="1.5"><path d="M4 32h32M8 26l12-14 6 6"/></svg><span class="num">02</span><div><h4>Fabrication</h4><span>Lorem ipsum dolor sit amet consectetur adipis</span></div></div>
  <div class="step" style="top:438px"><svg width="40" height="40" fill="none" stroke="var(--blue)" stroke-width="1.5"><rect x="6" y="10" width="18" height="12"/><path d="M24 16h10M12 22v12"/></svg><span class="num">03</span><div><h4>Powder Coating</h4><span>Lorem ipsum dolor sit amet consectetur adipiscing</span></div></div>
  <div class="step" style="top:512px"><svg width="40" height="40" fill="none" stroke="var(--blue)" stroke-width="1.5"><path d="M6 34L26 14M24 6a8 8 0 0010 10M8 8l24 24"/></svg><span class="num">04</span><div><h4>Installation</h4><span>Lorem ipsum dolor sit amet consectetur adipi</span></div></div>
  <a class="btn" style="left:128px;top:608px;width:242px;height:56px;font-size:13px">Get a Free Quote ↗</a>
  <div class="abs" role="img" aria-label="Slat gate and entry pillar overlooking the bay" style="left:713px;top:0;width:487px;height:658px;background:linear-gradient(180deg,#6f9cc4 0%,#5f8f7f 35%,#d9d4cc 60%,#2f332f 100%)"></div>
  <div class="abs" role="img" aria-label="Laser cutting sparks on metal" style="left:593px;top:322px;width:304px;height:392px;border:6px solid var(--white);background:radial-gradient(circle at 55% 40%,#ffcf7a,#c8641a 35%,#3a1a08 80%)"></div>
</section>

<section class="testimonials">
  <h2 class="display">Testimonials</h2>
  <div class="divider" style="left:554px;top:128px"></div>
  <svg class="abs" style="left:88px;top:290px" width="20" height="36" fill="none" stroke="var(--blue-light)" stroke-width="2"><path d="M18 2L2 18l16 16"/></svg>
  <svg class="abs" style="left:1093px;top:290px" width="20" height="36" fill="none" stroke="var(--blue-light)" stroke-width="2"><path d="M2 2l16 16L2 34"/></svg>
  <div class="quote" style="left:127px"><div class="display" style="color:var(--blue-light);font-size:60px;line-height:30px">“</div><p>"The workmanship was outstanding from start to finish. Our new electric gate and privacy screens have completely transformed our home."</p><div class="stars">★★★★★</div><div class="name">Customer Name</div></div>
  <div class="quote" style="left:608px"><div class="display" style="color:var(--blue-light);font-size:60px;line-height:30px">“</div><p>"The workmanship was outstanding from start to finish. Our new electric gate and privacy screens have completely transformed our home."</p><div class="stars">★★★★★</div><div class="name">Customer Name</div></div>
  <a class="btn" style="left:488px;top:474px;width:226px;height:52px;font-size:13px">Get a Free Quote ↗</a>
</section>

<section class="areas">
  <h2 class="display">Service Areas</h2>
  <div class="divider" style="left:554px;top:106px"></div>
  <div class="areas-card">
    <h3>Areas We Service</h3>
    <ul class="area-list">
      <li><svg width="12" height="16"><path d="M6 16C2 10 0 8 0 6a6 6 0 0112 0c0 2-2 4-6 10z" fill="var(--blue)"/></svg>Whitsundays</li>
      <li><svg width="12" height="16"><path d="M6 16C2 10 0 8 0 6a6 6 0 0112 0c0 2-2 4-6 10z" fill="var(--blue)"/></svg>Airlie Beach</li>
      <li><svg width="12" height="16"><path d="M6 16C2 10 0 8 0 6a6 6 0 0112 0c0 2-2 4-6 10z" fill="var(--blue)"/></svg>Bowen</li>
      <li><svg width="12" height="16"><path d="M6 16C2 10 0 8 0 6a6 6 0 0112 0c0 2-2 4-6 10z" fill="var(--blue)"/></svg>Ayr</li>
      <li><svg width="12" height="16"><path d="M6 16C2 10 0 8 0 6a6 6 0 0112 0c0 2-2 4-6 10z" fill="var(--blue)"/></svg>Townsville</li>
    </ul>
    <a class="btn" style="left:75px;top:330px;width:180px;height:42px;font-size:10px">Get a Free Quote ↗</a>
  </div>
  <div class="abs" role="img" aria-label="Satellite map of the coast from Townsville to the Whitsundays with location markers" style="left:612px;top:159px;width:508px;height:420px;background:linear-gradient(120deg,#1f3a2a 0%,#3a4a2c 40%,#1d5a6a 65%,#0d2a44 100%)"></div>
</section>

<section class="contact">
  <div class="abs" role="img" aria-label="Faded metal workshop backdrop" style="inset:0;background:linear-gradient(90deg,rgba(7,26,51,.25),rgba(0,0,0,0) 50%)"></div>
  <h2 class="display">Contact Us</h2>
  <div class="c-item" style="top:190px"><div class="ic"><svg width="18" height="18" viewBox="0 0 24 24" fill="var(--blue)"><path d="M6.6 10.8a15 15 0 006.6 6.6l2.2-2.2a1 1 0 011-.25 11 11 0 003.5.56 1 1 0 011 1V20a1 1 0 01-1 1A17 17 0 013 4a1 1 0 011-1h3.5a1 1 0 011 1 11 11 0 00.56 3.5 1 1 0 01-.25 1z"/></svg></div><div><b>Phone</b><span>(07) 4900 1122</span></div></div>
  <div class="c-item" style="top:283px"><div class="ic"><svg width="16" height="20"><path d="M8 20C3 13 0 10 0 8a8 8 0 0116 0c0 2-3 5-8 12z" fill="var(--blue)"/><circle cx="8" cy="8" r="3" fill="#fff"/></svg></div><div><b>Location</b><span>Whitsundays, Queensland</span></div></div>
  <div class="c-item" style="top:376px"><div class="ic"><svg width="18" height="14"><rect width="18" height="14" fill="var(--blue)"/><path d="M0 0l9 8 9-8" stroke="#fff" fill="none"/></svg></div><div><b>Email</b><span>hello@brellancoatworks.com.au</span></div></div>
  <div class="form">
    <h3>Request a Quote</h3>
    <div class="label" style="left:602px;top:136px">Full Name</div>
    <div class="label" style="left:852px;top:136px">Email address</div>
    <div class="field" style="left:602px;top:160px;width:245px">Name</div>
    <div class="field" style="left:856px;top:160px;width:248px">Email address</div>
    <div class="label" style="left:604px;top:226px">Phone number</div>
    <div class="label" style="left:855px;top:226px">Service Type</div>
    <div class="field" style="left:602px;top:247px;width:245px">Phone</div>
    <div class="field" style="left:856px;top:247px;width:248px">Select Service<svg style="position:absolute;right:16px;top:19px" width="12" height="8" fill="none" stroke="#333" stroke-width="2"><path d="M1 1l5 5 5-5"/></svg></div>
    <div class="label" style="left:600px;top:313px">Leave Message</div>
    <div class="field" style="left:602px;top:335px;width:502px;height:90px">Message</div>
    <a class="btn" style="left:602px;top:455px;width:194px;height:44px;background:var(--navy);font-size:13px">Submit Now ↗</a>
  </div>
</section>

<footer class="footer">
  <div class="abs logo" style="left:112px;top:137px;font-size:20px"><span class="logo-mark"></span>YOUR BUSINESS</div>
  <p class="abs" style="left:113px;top:182px;width:240px;font-size:10px;line-height:19px;color:#c4d3e2">Lorem ipsum dolor sit amet, consectetur adipiscing elit, sed do eiusmod tempor incididunt ut labore et dolore magna aliqua. Quis ipsum suspendisse ultrices gravida Risus</p>
  <div class="abs" style="left:113px;top:275px;display:flex;gap:4px"><span style="width:22px;height:22px;border-radius:50%;background:#fff"></span><span style="width:22px;height:22px;border-radius:50%;background:#fff"></span><span style="width:22px;height:22px;border-radius:50%;background:#fff"></span></div>
  <div class="f-col" style="left:404px"><h5>Navigation</h5><ul><li>Home</li><li>About Us</li><li>Services</li><li>Projects</li><li>Gallery</li><li>Contact</li></ul></div>
  <div class="f-col" style="left:558px"><h5>Services</h5><ul><li>Handrails</li><li>Privacy Slat Screens</li><li>Electric Gates</li><li>Pool Fencing</li><li>Glass Balustrades</li><li>Stainless Steel Fabrication</li><li>Powder Coated Aluminium</li></ul></div>
  <div class="f-col" style="left:738px"><h5>Area We Serve</h5><ul><li>Airlie Beach</li><li>Cannonvale</li><li>Proserpine</li><li>Bowen</li><li>Ayr</li><li>Home Hill</li><li>Townsville</li><li>Surrounding Areas</li></ul></div>
  <div class="f-col" style="left:922px"><h5>Contact</h5><ul style="line-height:16px"><li style="margin-bottom:14px">☏&nbsp;&nbsp;0491 570 006</li><li style="margin-bottom:14px">✉&nbsp;&nbsp;hello@brellancoatworks.com.au</li><li>⌖&nbsp;&nbsp;Whitsunday, QLD<br>&nbsp;&nbsp;&nbsp;&nbsp;Airlie Beach to Townsville</li></ul></div>
  <div class="f-bottom"><span>© 2025 Your Company . All Rights Reserved.</span><span>Privacy Policy | Terms &amp; Conditions | Sitemap</span></div>
</footer>

</body>
</html>
```